BHSC Business cards

We are an established dental practice that is looking for new business cards to match our new logo. We are looking for something unique and sophisticated.
BRIEF: Colours are black, silver and white. Include the company name, logo (including “Pelwick Heath Dental Care”) and phone number “03 9415 2876”.
Front - Include the company name, logo (including “Pelwick Heath Dental Care”) and phone number “03 9415 2876”.
Back - Include the company name,  “Pelwick Heath Dental Care”, phone number “03 9415 2876”. address "64A Tindle Street, Pelwick Heath, Vic 3187", "Email reception@pelwickheathdentalcare.com.au", the Dentist Name " Dr ................................"  Your next appointment "Day, date and time(am/pm)".  3 lines for 3 appointments please, and at the bottom "IF UNABLE TO KEEP THIS APPOINTMENT 48 HOURS NOTICE IS REQUIRED."
Try and be creative and different with the design, i've added an image for inspiration

Target Market(s)
ALL in need of dental
Industry/Entity Type
Dental Clinic
Look and feel
Each slider illustrates characteristics of the customer's brand and the style your logo design should communicate.

```html
<!DOCTYPE html>
<html lang="en">
<head>
<meta charset="utf-8">
<title>Pelwick Heath Dental Care – Business Cards</title>
<link href="https://fonts.googleapis.com/css2?family=Lato:wght@300;400;700;900&display=swap" rel="stylesheet">
<style>
  :root {
    --stage: #dcdcdc;
    --card: #f4f4f3;
    --ink: #1c1c1c;
    --silver: #8a8a8a;
    --rule: #6f6f6f;
    --band: #161616;
    --band-text: #f2f2f2;
  }
  * { box-sizing: border-box; margin: 0; padding: 0; }
  html, body { width: 1200px; height: 900px; overflow: hidden; }
  body {
    background: var(--stage);
    font-family: "Lato", sans-serif;
    color: var(--ink);
    position: relative;
  }
  .card {
    position: absolute;
    left: 300px;
    width: 600px;
    height: 343px;
    background: var(--card);
    box-shadow: 0 6px 18px rgba(0,0,0,0.12);
    overflow: hidden;
  }
  .card--front { top: 72px; }
  .card--back { top: 470px; }

  /* Front */
  .brand {
    position: absolute;
    left: 112px;
    top: 132px;
    display: flex;
    align-items: center;
    gap: 16px;
  }
  .brand__dot {
    width: 64px; height: 64px;
    border-radius: 50%;
    background: var(--ink);
    flex: none;
  }
  .brand__text { line-height: 1; }
  .brand__name {
    font-weight: 900;
    font-size: 30px;
    letter-spacing: 1px;
    text-transform: uppercase;
  }
  .brand__sub {
    margin-top: 6px;
    display: flex;
    gap: 10px;
    font-weight: 900;
    font-size: 17px;
    letter-spacing: 3px;
    text-transform: uppercase;
  }
  .brand__phone { letter-spacing: 1.5px; }

  /* Back */
  .header {
    position: absolute;
    left: 36px; right: 36px; top: 30px;
    display: flex;
    align-items: center;
    padding-bottom: 14px;
    border-bottom: 1px solid var(--rule);
  }
  .dentist__name { font-weight: 900; font-size: 27px; line-height: 1.05; }
  .dentist__role { font-weight: 400; font-size: 15px; color: var(--silver); margin-top: 3px; }
  .header__divider {
    width: 1px; height: 46px;
    background: var(--rule);
    margin: 0 18px;
  }
  .contact { font-size: 14px; line-height: 1.6; font-weight: 400; }

  .appointments {
    position: absolute;
    left: 36px; right: 36px; top: 128px;
    display: flex;
    gap: 14px;
  }
  .appointments__label {
    font-weight: 700;
    font-size: 20px;
    letter-spacing: 0.5px;
    white-space: nowrap;
    padding-top: 2px;
  }
  .appointments__list { flex: 1; display: flex; flex-direction: column; gap: 18px; }
  .slot {
    display: flex;
    align-items: baseline;
    font-size: 17px;
    white-space: nowrap;
  }
  .slot__fill {
    border-bottom: 2px dotted var(--ink);
    margin: 0 5px;
    transform: translateY(-4px);
  }
  .slot__fill--date { flex: 3; }
  .slot__fill--time { flex: 1; }

  .notice {
    position: absolute;
    left: 0; right: 0; bottom: 0;
    height: 48px;
    background: var(--band);
    color: var(--band-text);
    display: flex;
    align-items: center;
    justify-content: center;
    font-size: 14px;
    letter-spacing: 0.6px;
    text-transform: uppercase;
  }
</style>
</head>
<body>

  <section class="card card--front">
    <div class="brand">
      <div class="brand__dot"></div>
      <div class="brand__text">
        <div class="brand__name">Pelwick Heath</div>
        <div class="brand__sub"><span>Dental Care</span><span>—</span><span class="brand__phone">03 9415 2876</span></div>
      </div>
    </div>
  </section>

  <section class="card card--back">
    <header class="header">
      <div class="dentist">
        <div class="dentist__name">DR.OWEN MARSH</div>
        <div class="dentist__role">Senior Dentist</div>
      </div>
      <div class="header__divider"></div>
      <div class="contact">
        <div>64A Tindle Street, Pelwick Heath, Vic 3187</div>
        <div>reception@pelwickheathdentalcare.com.au</div>
      </div>
    </header>

    <div class="appointments">
      <div class="appointments__label">NEXT APPOINTMENT:</div>
      <div class="appointments__list">
        <div class="slot">Date<span class="slot__fill slot__fill--date"></span>At<span class="slot__fill slot__fill--time"></span>am/pm</div>
        <div class="slot">Date<span class="slot__fill slot__fill--date"></span>At<span class="slot__fill slot__fill--time"></span>am/pm</div>
        <div class="slot">Date<span class="slot__fill slot__fill--date"></span>At<span class="slot__fill slot__fill--time"></span>am/pm</div>
      </div>
    </div>

    <footer class="notice">If unable to keep this appointment 48 hours notice is required</footer>
  </section>

</body>
</html>
```